Retail Jewelry Business Card Design Project

We are in need of a new business card design for a retail jewelry store. This store is in the business of fine jewelry including but not specific to bridal jewelry, diamonds, designer jewelry and watches.

This store has been in business for 20 years but continues to strive for a modern professional appeal. The main colors use for this business are a royal blue, white and silver.

Target Market(s)

Target market is ages 18-50

Industry/Entity Type

Jewelry

Requirements
Must have
• Sales Person Name
Sales Person Email Address

Store Address
Store Phone
Website

Standard business card size. No odd shapes or sizes.
Nice to have
• Overall modern feel for card.

We have thought that a design with a nice feature of the logo on the back of the card would be nice but open to ideas.
Should not have
• No specific images of jewelry should be used.

```html
<!DOCTYPE html>
<html lang="en">
<head>
<meta charset="utf-8">
<title>Laurel Grant Fine Jewelry – Business Card</title>
<link href="https://fonts.googleapis.com/css2?family=Open+Sans:wght@400&display=swap" rel="stylesheet">
<style>
  :root {
    --royal: #262c6e;
    --royal-ink: #2c3179;
    --royal-glow: #3b51a8;
    --royal-deep: #1c2259;
    --silver: #c9ccd6;
    --silver-dark: #8d909c;
    --periwinkle: #a9b1dd;
    --white: #ffffff;
    --backdrop: #eeeae4;
  }
  * { margin: 0; padding: 0; box-sizing: border-box; }
  html, body {
    width: 1200px; height: 1000px; overflow: hidden;
    background: var(--backdrop);
    font-family: "Open Sans", Arial, sans-serif;
  }
  .sheet {
    position: relative; width: 1200px; height: 1000px;
  }
  .card {
    position: absolute; top: 349px;
    width: 536px; height: 302px;
    border-radius: 12px; overflow: hidden;
    box-shadow: 0 6px 14px rgba(0,0,0,0.28);
  }
  .card-front { left: 46px; background: var(--white); }
  .card-back {
    left: 617px;
    background: radial-gradient(ellipse 60% 70% at 50% 45%, var(--royal-glow) 0%, var(--royal) 55%, var(--royal-deep) 100%);
  }
  .wordmark {
    position: absolute; left: 0; right: 0; text-align: center;
    font-weight: 400; line-height: 1;
  }
  .wordmark-name { display: block; font-size: 31px; letter-spacing: 0.5px; }
  .wordmark-tag { display: block; font-size: 12px; letter-spacing: 2.5px; margin-top: 6px; }
  .card-front .wordmark { top: 30px; color: var(--royal-ink); }
  .card-back .wordmark { top: 126px; color: var(--white); }
  .holder-name {
    position: absolute; top: 110px; left: 0; right: 0; text-align: center;
    font-size: 22px; color: var(--royal-ink); font-weight: 400;
  }
  .wave { position: absolute; left: 0; top: 0; width: 536px; height: 302px; }
  .contact {
    position: absolute; list-style: none; color: var(--white); font-size: 14px;
  }
  .contact li { display: flex; align-items: flex-start; height: 25px; }
  .contact svg { width: 18px; height: 18px; margin-right: 7px; flex: none; margin-top: 1px; }
  .contact-online { left: 18px; top: 227px; }
  .contact-store { left: 342px; top: 227px; }
  .address-lines { line-height: 17px; }
</style>
</head>
<body>
<main class="sheet">

  <section class="card card-front" aria-label="Business card front">
    <svg class="wave" viewBox="0 0 536 302" aria-hidden="true">
      <defs>
        <linearGradient id="silverSweep" x1="0" x2="1" y1="0" y2="0">
          <stop offset="0" stop-color="var(--silver-dark)"/>
          <stop offset="0.35" stop-color="var(--white)"/>
          <stop offset="0.7" stop-color="var(--silver)"/>
          <stop offset="1" stop-color="var(--silver-dark)" stop-opacity="0"/>
        </linearGradient>
      </defs>
      <path d="M0,160 C120,172 230,178 330,172 C250,184 140,186 0,178 Z" fill="var(--periwinkle)"/>
      <path d="M0,174 C130,190 250,190 360,170 C250,196 120,200 0,190 Z" fill="url(#silverSweep)"/>
      <path d="M0,186 C150,200 280,186 380,166 C440,155 490,154 536,156 L536,302 L0,302 Z" fill="var(--royal)"/>
    </svg>

    <h1 class="wordmark">
      <span class="wordmark-name">Laurel Grant</span>
      <span class="wordmark-tag">FINE JEWELRY</span>
    </h1>
    <p class="holder-name">Laurel Grant Whitmore</p>

    <ul class="contact contact-online">
      <li>
        <svg viewBox="0 0 18 18"><circle cx="9" cy="9" r="8.5" fill="var(--white)"/><circle cx="9" cy="9" r="3" fill="none" stroke="var(--royal)" stroke-width="1.6"/><path d="M12,6.5 V10.5 Q12,12.5 13.5,12 M12,9 A3,3 0 0 1 12,9" fill="none" stroke="var(--royal)" stroke-width="1.6"/></svg>
        laurel@laurelgrantjewelry.com
      </li>
      <li>
        <svg viewBox="0 0 18 18"><circle cx="9" cy="9" r="8.5" fill="var(--white)"/><g fill="none" stroke="var(--royal)" stroke-width="1.1"><circle cx="9" cy="9" r="6"/><ellipse cx="9" cy="9" rx="2.6" ry="6"/><path d="M3,9 H15 M4,6 H14 M4,12 H14"/></g></svg>
        www.laurelgrantjewelry.com
      </li>
    </ul>

    <ul class="contact contact-store">
      <li>
        <svg viewBox="0 0 18 18"><circle cx="9" cy="9" r="8.5" fill="var(--white)"/><path d="M5.5,4.5 L7.3,4.3 L8.2,7 L7,8 Q8,10.3 10,11 L11,9.8 L13.7,10.7 L13.5,12.5 Q9.5,13.5 6.8,10.8 Q4.3,8.2 5.5,4.5 Z" fill="var(--royal)"/></svg>
        0198 765 432
      </li>
      <li>
        <svg viewBox="0 0 18 18"><circle cx="9" cy="9" r="8.5" fill="var(--white)"/><path d="M9,3.5 A3.8,3.8 0 0 1 12.8,7.3 C12.8,10 9,14.5 9,14.5 C9,14.5 5.2,10 5.2,7.3 A3.8,3.8 0 0 1 9,3.5 Z" fill="var(--royal)"/><circle cx="9" cy="7.3" r="1.5" fill="var(--white)"/></svg>
        <span class="address-lines">2870 Bayview Avenue<br>Port Avery, FL 32455</span>
      </li>
    </ul>
  </section>

  <section class="card card-back" aria-label="Business card back">
    <h2 class="wordmark">
      <span class="wordmark-name">Laurel Grant</span>
      <span class="wordmark-tag">FINE JEWELRY</span>
    </h2>
  </section>

</main>
</body>
</html>
```